I need a website built for my organization.
We are the world's largest network of music producers.
The website should be professional, sharp, and high quality., We need a website built for The Halvern Sound Guild. We are one of the World's largest association of music producers.
The site must be professional, sharp, and high quality., I need a website built for my organization.
The site must be professional, sharp, and high quality.
Somewhere in the top half of the site there should be a form for the user to fill out. The details of the form are as follows:
Title (large and bold): Contact Us or Submit Your Music
Fields to include (* = required): First Name*, Last Name*, Age, Zip Code, Email Address*, Daytime Phone, Evening Phone, Comments
Then, there will be a "submit" button to proceed to next step of form. Just below the "submit" button, should be the following verbiage: "After submitting, you will have the opportunity to upload demos of your music (optional) and provide other pertinent information about yourself, band, or group."
Target Market(s)
Music producers and aspiring musicians
Industry/Entity Type
Group
Colors
Designer to choose colors to be used in the design.
Look and feel

```html
<!DOCTYPE html>
<html lang="en">
<head>
<meta charset="utf-8">
<title>The Halvern Sound Guild – Member Profile</title>
<link href="https://fonts.googleapis.com/css2?family=Raleway:ital,wght@0,400;0,500;0,600;1,400&family=Roboto:ital@1&display=swap" rel="stylesheet">
<style>
  :root{
    --accent:#ff5a1f;
    --ink:#222628;
    --muted:#a9a9a9;
    --body-text:#b9b9b9;
    --rule:#c8c8c8;
    --control:#cfcfcf;
    --night:#1e2a2e;
    --paper:#ffffff;
  }
  *{margin:0;padding:0;box-sizing:border-box}
  html,body{width:1200px;height:1141px;overflow:hidden;background:var(--paper)}
  body{position:relative;font-family:"Raleway",Arial,sans-serif}

  .profile{position:absolute;left:0;top:0;width:682px;height:1141px;background:var(--paper)}
  .gallery{position:absolute;left:682px;top:0;width:518px;height:1141px}

  .form-note{position:absolute;left:0;top:0;width:518px;height:103px;background:linear-gradient(180deg,#1b2529,#223035);overflow:hidden}
  .form-note p{position:absolute;left:95px;top:-8px;white-space:nowrap;color:#fff;font:italic 17px "Roboto",Arial,sans-serif}

  .portrait{position:absolute;left:0;width:518px}
  .portrait--featured{top:103px;height:519px;background:radial-gradient(ellipse at 55% 45%,#ff7a3e 0%,#ff5a1f 45%,#c23a0c 100%)}
  .portrait--next{top:622px;height:519px;background:radial-gradient(ellipse at 60% 50%,#5a5a5a 0%,#262626 55%,#080808 100%)}
  .pointer{position:absolute;left:666px;top:207px}

  .close-btn{position:absolute;left:528px;top:100px;width:78px;height:78px;border-radius:50%;background:var(--accent);display:flex;align-items:center;justify-content:center}

  .avatar{position:absolute;left:54px;top:175px;width:166px;height:166px;border-radius:50%;background:radial-gradient(circle at 50% 40%,#d8d8d8,#7d7d7d 70%,#4a4a4a);border:3px solid #e4e4e4}

  .member-name{position:absolute;left:250px;top:203px;font-size:29px;font-weight:600;color:var(--ink);letter-spacing:.3px}
  .member-meta{position:absolute;left:247px;top:248px;list-style:none}
  .member-meta li{display:flex;align-items:center;height:38px;font-size:22px}
  .member-meta .location{color:var(--muted)}
  .member-meta .site{color:var(--accent);font-size:21px}
  .member-meta svg{margin-right:12px}

  .bio{position:absolute;left:55px;top:400px;width:560px;font-size:18.6px;line-height:31px;color:var(--body-text)}
  .bio span{display:block;white-space:nowrap}
  .bio .tail{margin-top:4px}
  .bio .para2{margin-top:31px}

  .divider{position:absolute;left:55px;width:548px;border-top:2px dotted var(--rule)}
  .divider--top{top:799px}
  .divider--bottom{top:1075px}

  .player-controls{position:absolute;left:0;top:0}
  .track-title{position:absolute;left:54px;top:999px;font-size:21px;color:var(--accent)}
  .track-time{position:absolute;right:85px;top:1000px;font-size:18px;font-style:italic;color:var(--muted)}
  .stub-line{position:absolute;left:55px;top:1138px;width:160px;border-top:2px solid #e2e2e2}
</style>
</head>
<body>

<section class="profile">
  <div class="close-btn" aria-label="Close profile">
    <svg width="26" height="26" viewBox="0 0 26 26"><path d="M3 3 L23 23 M23 3 L3 23" stroke="#fff" stroke-width="3" stroke-linecap="round"/></svg>
  </div>

  <div class="avatar" role="img" aria-label="Portrait photo of Marion Keller"></div>

  <h1 class="member-name">Marion Keller</h1>
  <ul class="member-meta">
    <li class="location">
      <svg width="18" height="26" viewBox="0 0 18 26"><path d="M9 1a8 8 0 0 0-8 8c0 6 8 16 8 16s8-10 8-16a8 8 0 0 0-8-8z" fill="#c4c4c4"/><circle cx="9" cy="9" r="3" fill="#fff"/></svg>
      Ashford, UK
    </li>
    <li class="site">
      <svg width="22" height="16" viewBox="0 0 22 16"><rect x="0" y="0" width="22" height="16" fill="var(--accent)"/><path d="M0 0 L11 9 L22 0" fill="none" stroke="#fff" stroke-width="1.6"/></svg>
      www.marionkeller.com
    </li>
  </ul>

  <div class="bio">
    <p>
      <span>Lorem ipsum dolor sit amet, consectetur adipiscing elit.</span>
      <span>Etiam euismod massa sit amet purus lobortis hendrerit.</span>
      <span>Vestibulum sed diam nec nibh egestas vulputate. Nunc</span>
      <span>porttitor tempor nulla, varius egestas turpis volutpat at.</span>
      <span>Maecenas feugiat, metus nec iaculis consectetur, ligula</span>
      <span>turpis placerat urna, quis varius urna tortor id quam.</span>
      <span class="tail">Integer sit amet sollicitudin lacus.</span>
    </p>
    <p class="para2">
      <span>Ut venenatis est id ipsum eleifend malesuada. Phasellus</span>
      <span>viverra, orci sit amet fringilla vehicula, tortor lectus dapibus</span>
      <span>quam, ac euismod neque ipsum in nisi.</span>
    </p>
  </div>

  <div class="divider divider--top"></div>

  <svg class="player-controls" width="682" height="1000" viewBox="0 0 682 1000" aria-label="Audio player controls">
    <!-- previous -->
    <circle cx="89" cy="886" r="33" fill="none" stroke="var(--control)" stroke-width="2.5"/>
    <path d="M88 876 L76 886 L88 896 Z M101 876 L89 886 L101 896 Z" fill="#bdbdbd"/>
    <!-- pause -->
    <circle cx="181" cy="886" r="45" fill="none" stroke="var(--control)" stroke-width="2.5"/>
    <rect x="170" y="872" width="5" height="28" fill="#bdbdbd"/>
    <rect x="187" y="872" width="5" height="28" fill="#bdbdbd"/>
    <!-- next -->
    <circle cx="274" cy="886" r="33" fill="none" stroke="var(--control)" stroke-width="2.5"/>
    <path d="M263 876 L275 886 L263 896 Z M276 876 L288 886 L276 896 Z" fill="#bdbdbd"/>
    <!-- volume -->
    <rect x="410" y="878" width="173" height="14" rx="7" fill="var(--night)"/>
    <rect x="413" y="881" width="121" height="8" rx="4" fill="#fff"/>
    <path d="M590 880 q4 5 0 10 M595 877 q6 8 0 16 M600 874 q8 11 0 22" fill="none" stroke="var(--night)" stroke-width="1.8"/>
    <!-- progress -->
    <line x1="55" y1="969" x2="600" y2="969" stroke="#dcdcdc" stroke-width="2"/>
    <line x1="55" y1="969" x2="183" y2="969" stroke="var(--accent)" stroke-width="2.5"/>
    <circle cx="183" cy="969" r="10" fill="var(--accent)"/>
  </svg>

  <p class="track-title">Marion Keller - Track 4</p>
  <p class="track-time">1.24/4.53</p>

  <div class="divider divider--bottom"></div>
  <div class="stub-line"></div>
</section>

<aside class="gallery">
  <div class="form-note"><p>(optional) and provide other pertinent information about yourself, band, or group.</p></div>
  <div class="portrait portrait--featured" role="img" aria-label="Orange-toned portrait photo of the featured member in a hooded top"></div>
  <div class="portrait portrait--next" role="img" aria-label="Black and white close-up portrait photo of another member wearing glasses"></div>
</aside>

<svg class="pointer" width="17" height="34" viewBox="0 0 17 34"><path d="M17 0 L0 17 L17 34 Z" fill="var(--accent)"/></svg>

</body>
</html>
```